Looking for updated Letterhead and Compliments Slips to go with our new updated logo. This stationary will be used for letters to suppliers and customers so needs to be practical while also quite classic.

We are an engineering company so needs to be clean and precise

Target Market(s)

SME'S and large automotive customers

Industry/Entity Type

Automotive

Font styles to use
Sans Serif

Colors
85acd3
0356a4
0792cd
33a6d7
85abd2
ffffff

Requirements
Must have
• Address details as below
• KT Fabrications Limited
• Hallmere Road
• Kelsworth
• Marrowshire
• LP47 9XZ, UK
• Telephone: +44 (0)1632 960418
• Fax: +44 (0)1632 960733
• Email: sales@ktfabrications.example
• Web: www.ktfabrications.example
Nice to have
• Nice to have some element of being a British Manufacturer

```html
<!DOCTYPE html>
<html lang="en">
<head>
<meta charset="utf-8">
<title>KT Fabrications Letterhead</title>
<link href="https://fonts.googleapis.com/css2?family=Open+Sans:ital,wght@0,400;0,600;0,700;1,400&display=swap" rel="stylesheet">
<style>
  :root {
    --brand-blue: #0356a4;
    --brand-sky: #85acd3;
    --band-grey: #6b6b6d;
    --text-dark: #3a3a3c;
    --paper: #ffffff;
    --backdrop: #e9e9ea;
  }
  * { margin: 0; padding: 0; box-sizing: border-box; }
  html, body { width: 1200px; height: 878px; overflow: hidden; }
  body {
    background: var(--backdrop);
    font-family: "Open Sans", Arial, sans-serif;
    color: var(--text-dark);
  }
  .letterhead {
    position: absolute;
    left: 305px;
    top: 22px;
    width: 590px;
    height: 834px;
    background: var(--paper);
    box-shadow: 0 6px 24px rgba(0,0,0,.15);
    overflow: hidden;
  }
  .header-swoosh { position: absolute; left: 0; top: 0; width: 590px; height: 90px; }
  .brand-name {
    position: absolute;
    right: 52px;
    top: 112px;
    display: flex;
    align-items: center;
    gap: 8px;
    font-size: 15px;
    font-weight: 600;
    letter-spacing: 4px;
    text-transform: uppercase;
    color: var(--brand-blue);
  }
  .brand-dot { width: 10px; height: 10px; border-radius: 50%; background: var(--brand-sky); }
  .recipient {
    position: absolute;
    left: 52px;
    top: 168px;
    font-size: 9.5px;
    font-style: italic;
    line-height: 1.45;
  }
  .letter-body {
    position: absolute;
    left: 52px;
    top: 250px;
    width: 486px;
    font-size: 9.5px;
    line-height: 1.5;
  }
  .letter-body p { margin-bottom: 9px; }
  .sign-off { margin-top: 18px; font-style: italic; }
  .footer {
    position: absolute;
    left: 0;
    bottom: 0;
    width: 590px;
  }
  .footer-band {
    background: var(--band-grey);
    height: 56px;
    display: flex;
    align-items: center;
    justify-content: space-between;
    padding: 0 40px;
    color: #fff;
    font-size: 8px;
    line-height: 1.6;
  }
  .footer-gap { height: 5px; background: var(--paper); }
  .footer-stripe { height: 22px; background: var(--brand-blue); }
  .company-block strong { font-weight: 700; display: block; }
  .contact-line { display: flex; align-items: center; gap: 5px; }
  .contact-line svg { width: 8px; height: 8px; fill: #fff; flex: none; }
</style>
</head>
<body>
<main class="letterhead">
  <svg class="header-swoosh" viewBox="0 0 590 90" aria-hidden="true">
    <path d="M0 0 H590 V62 C440 20 240 12 0 12 Z" fill="var(--brand-blue)"/>
    <path d="M0 17 C240 17 440 25 590 68 V76 C440 33 240 24 0 24 Z" fill="var(--band-grey)"/>
  </svg>

  <div class="brand-name"><span class="brand-dot"></span>KT Fabrications</div>

  <address class="recipient">
    Mr. Daniel Marsh<br>
    Managing Director<br>
    USA Investor<br>
    48 Orchard Avenue<br>
    USA
  </address>

  <section class="letter-body">
    <p>Lorem ipsum dolor sit amet, consectetuer adipiscing elit. Nam cursus. Morbi ut mi. Nullam enim leo, egestas id, condimentum at, laoreet mattis, massa. Sed eleifend nonummy diam. Praesent mauris ante, elementum et, bibendum at, posuere sit amet, nibh. Duis tincidunt lectus quis dui viverra vestibulum.</p>
    <p>Suspendisse vulputate aliquam dui. Nulla elementum dui ut augue. Aliquam vehicula mi at mauris. Maecenas placerat, nisl at consequat rhoncus, sem nunc gravida justo, quis eleifend arcu velit quis lacus. Morbi magna magna, tincidunt a, mattis non, imperdiet vitae, tellus. Sed odio est, auctor ac, sollicitudin in, consequat vitae, orci. Fusce id felis. Vivamus sollicitudin.</p>
    <p>Metus eget eros. Pellentesque habitant morbi tristique senectus et netus et malesuada fames ac turpis egestas. In posuere felis nec tortor. Pellentesque faucibus. Ut accumsan ultricies elit. Maecenas at justo id velit placerat molestie. Donec dictum lectus non odio. Cras a ante vitae enim iaculis aliquam.</p>
    <p>Mauris nunc quam, venenatis nec, euismod sit amet, egestas placerat, est. Pellentesque habitant morbi tristique senectus et netus et malesuada fames ac turpis egestas. Cras id elit. Integer quis urna. Ut ante enim, dapibus malesuada, fringilla eu, condimentum quis, tellus. Aenean porttitor eros vel dolor. Donec convallis pede venenatis nibh. Duis quam. Nam eget.</p>
    <p>Thank you for being one of our valued customers.</p>
    <p class="sign-off">Name Here<br>CEO</p>
  </section>

  <footer class="footer">
    <div class="footer-band">
      <div class="company-block contact-line">
        <svg viewBox="0 0 10 10"><path d="M5 0a3.5 3.5 0 0 0-3.5 3.5C1.5 6 5 10 5 10s3.5-4 3.5-6.5A3.5 3.5 0 0 0 5 0zm0 5a1.4 1.4 0 1 1 0-2.8A1.4 1.4 0 0 1 5 5z"/></svg>
        <div><strong>KT Fabrications Limited</strong>Hallmere Road, Kelsworth, Marrowshire LP47 9XZ, UK</div>
      </div>
      <div>
        <div class="contact-line"><svg viewBox="0 0 10 10"><path d="M2 0l2 2.5-1 1.2a6 6 0 0 0 3.3 3.3l1.2-1L10 8l-1.2 1.8C4.5 10 0 5.5.2 1.2z"/></svg>+44 (0)1632 960418</div>
        <div class="contact-line"><svg viewBox="0 0 10 10"><rect x="1" y="3" width="8" height="6" rx="1"/><rect x="3" y="0" width="4" height="3"/></svg>+44 (0)1632 960733</div>
      </div>
      <div>
        <div class="contact-line"><svg viewBox="0 0 10 10"><path d="M0 2h10v6H0zM0 2l5 3.5L10 2" stroke="#6b6b6d" stroke-width=".8"/></svg>sales@ktfabrications.example</div>
        <div class="contact-line"><svg viewBox="0 0 10 10"><circle cx="5" cy="5" r="5"/></svg>www.ktfabrications.example</div>
      </div>
    </div>
    <div class="footer-gap"></div>
    <div class="footer-stripe"></div>
  </footer>
</main>
</body>
</html>
```